" Travessa - Somos uma empresa de consultoria especializada em treinamentos presenciais e à distância (on-line) em disciplinas ligadas à Administraçao de Empresas e Informática. "

```html
<!DOCTYPE html>
<html lang="pt-BR">
<head>
<meta charset="utf-8">
<title>Travessa — Cartão de visita</title>
<link rel="stylesheet" href="https://fonts.googleapis.com/css2?family=Questrial&family=Open+Sans:wght@400;700&display=swap">
<style>
  :root {
    --green: #2f6d33;
    --green-dark: #1e4a22;
    --green-light: #4e8c45;
    --grey-text: #7d7f82;
    --grey-light: #b9bbbd;
    --paper: #ffffff;
    --stage: #efefef;
    --white: #ffffff;
  }
  * { box-sizing: border-box; margin: 0; padding: 0; }
  html, body { width: 1200px; height: 1200px; overflow: hidden; }
  body {
    background: var(--stage);
    font-family: "Open Sans", sans-serif;
    display: flex;
    flex-direction: column;
    align-items: center;
    padding-top: 50px;
    gap: 40px;
  }
  .card {
    width: 760px;
    height: 420px;
    position: relative;
    overflow: hidden;
    flex: none;
    box-shadow: 0 10px 30px rgba(0,0,0,0.18);
  }
  .card--back {
    background: linear-gradient(160deg, var(--green-light) 0%, var(--green) 45%, var(--green-dark) 100%);
    color: var(--white);
    display: flex;
    flex-direction: column;
    align-items: center;
    padding-top: 60px;
  }
  .card--back .edge-band {
    position: absolute; left: 0; right: 0; bottom: 38px; height: 10px;
    background: var(--white);
  }
  .card--back .edge-base {
    position: absolute; left: 0; right: 0; bottom: 0; height: 38px;
    background: var(--green-dark);
  }
  .brand {
    display: flex; align-items: center; gap: 16px;
    font-family: "Questrial", sans-serif;
    letter-spacing: 0.12em;
    text-transform: uppercase;
    white-space: nowrap;
  }
  .brand__square { display: block; flex: none; }
  .card--back .brand { font-size: 34px; color: var(--white); }
  .card--back .brand__square { width: 40px; height: 40px; background: var(--white); }
  .holder {
    margin-top: 40px;
    font-weight: 700; font-size: 19px; letter-spacing: 0.04em;
    white-space: nowrap;
  }
  .holder .sep { margin: 0 14px; font-weight: 400; opacity: 0.8; }
  .contacts {
    margin-top: 22px;
    display: flex; gap: 30px; font-size: 13px;
    white-space: nowrap;
  }
  .contact { display: flex; align-items: center; gap: 8px; }
  .contact__icon { width: 18px; height: 18px; flex: none; }
  .contact__icon--plain { background: var(--white); }
  .address { margin-top: 14px; font-size: 13px; opacity: 0.95; white-space: nowrap; }

  .card--front {
    background: var(--paper);
    display: flex; flex-direction: column; align-items: center; justify-content: center;
  }
  .card--front .edge-band {
    position: absolute; left: 0; right: 0; bottom: 0; height: 16px;
    background: var(--green);
  }
  .card--front .brand { font-size: 64px; color: var(--grey-text); }
  .card--front .brand__square { width: 56px; height: 56px; background: var(--green); }
  .url {
    margin-top: 14px; font-size: 14px; letter-spacing: 0.35em; color: var(--grey-light);
  }

  .lockup {
    margin-top: 10px;
    width: 1200px; flex: 1;
    background: var(--white);
    display: flex; align-items: center; justify-content: center;
  }
  .lockup .brand { font-size: 40px; color: #55585b; }
  .lockup .brand__square { width: 42px; height: 42px; background: var(--green); }
</style>
</head>
<body>
  <section class="card card--back" aria-label="Verso do cartão">
    <div class="brand"><span class="brand__square"></span>Travessa</div>
    <p class="holder">NOME E SOBRENOME<span class="sep">|</span>SÓCIO FUNDADOR</p>
    <div class="contacts">
      <span class="contact">
        <svg class="contact__icon" viewBox="0 0 18 18" aria-hidden="true"><rect width="18" height="18" rx="2" fill="#fff"/><path d="M5 4c1 0 1.5 2 1.5 2.5S5.5 7.5 5.8 8.3c.5 1.3 2.5 3.3 3.9 3.9.8.3 1.3-.7 1.8-.7s2.5.5 2.5 1.5-1 2-2 2C7.5 15 3 10.5 3 6c0-1 1-2 2-2z" fill="#2f6d33"/></svg>
        (00) 0000-0000
      </span>
      <span class="contact">
        <svg class="contact__icon" viewBox="0 0 18 18" aria-hidden="true"><rect width="18" height="18" rx="2" fill="#fff"/><path d="M3.5 5.5h11v7h-11z M3.5 5.5l5.5 4 5.5-4" fill="none" stroke="#2f6d33" stroke-width="1.4"/></svg>
        contato@travessaead.com.br
      </span>
      <span class="contact"><span class="contact__icon contact__icon--plain"></span>/travessaead</span>
      <span class="contact"><span class="contact__icon contact__icon--plain"></span>/travessaead</span>
    </div>
    <p class="address">Rua Exemplo do Endereço, 000 - São Paulo/SP - CEP 00000-000</p>
    <span class="edge-band"></span>
    <span class="edge-base"></span>
  </section>

  <section class="card card--front" aria-label="Frente do cartão">
    <div class="brand"><span class="brand__square"></span>Travessa</div>
    <p class="url">www.travessaead.com.br</p>
    <span class="edge-band"></span>
  </section>

  <footer class="lockup">
    <div class="brand"><span class="brand__square"></span>Travessa</div>
  </footer>
</body>
</html>
```